Wexbridge Home Services Web Site

Design Web site with 3-4 pages: Home, About Us, Services and Order form / Schedule Appointment (which will likely be link to Tallyo App and Ledgerpine integration.)
Services include: Dryer Vent Cleaning, AC Cleaning, Difficult-to-Reach Light Bulb replacement, Wood Repair and Home Maintenance Plans including Fire Safety Checks and Filter Replacement.

Target Market(s)

Luxury Home Owners, Professionals (Dr's/lawyers) and Seniors

Industry/Entity Type

Home Maintenance

Coding

Coded - Design and coding required

Requirements
Must have
• Tagline - Where Home Maintenance is Effortless

```html
<!DOCTYPE html>
<html lang="en">
<head>
<meta charset="utf-8">
<title>Wexbridge Home Services</title>
<link href="https://fonts.googleapis.com/css2?family=Montserrat:wght@400;500;600;700&display=swap" rel="stylesheet">
<style>
:root{
  --gold:#e3ab2c;
  --gold-dark:#d49c1c;
  --slate:#5b5b5e;
  --slate-dark:#4c4c4f;
  --ink:#3a3a3c;
  --muted:#6e6e72;
  --mist:#f1f1f1;
  --white:#ffffff;
}
*{box-sizing:border-box;margin:0;padding:0}
html,body{width:1200px;height:4967px;overflow:hidden}
body{position:relative;background:var(--white);font-family:'Montserrat',sans-serif;color:var(--ink)}
.abs{position:absolute}
.btn{position:absolute;display:flex;align-items:center;justify-content:center;gap:8px;border-radius:30px;font-weight:600;text-transform:uppercase;letter-spacing:.5px}
.btn-gold{background:var(--gold);color:var(--white)}
.btn-slate{background:var(--slate);color:var(--white)}
.btn-ghost{border:1.5px solid var(--white);color:var(--white)}
.wordmark{color:var(--gold);font-weight:700;text-transform:uppercase;letter-spacing:2px;text-align:center;line-height:1.1}
.photo{position:absolute;overflow:hidden}
h2.section-title{position:absolute;left:0;width:1200px;text-align:center;font-size:36px;font-weight:700;text-transform:uppercase;color:var(--slate-dark);letter-spacing:.5px}
.swoosh{position:absolute;height:5px;border-radius:50%;background:var(--gold)}

/* hero */
.hero{position:absolute;left:0;top:0;width:1200px;height:705px;background:var(--slate);border-radius:0 0 50% 50%/0 0 90px 90px;overflow:hidden}
.hero-photo{position:absolute;left:560px;top:0;width:640px;height:705px;background:linear-gradient(120deg,#6b6b6e 0%,#a89a86 45%,#d8c7a8 70%,#b98c55 100%)}
.topbar{position:absolute;top:22px;display:flex;align-items:center;gap:10px;color:var(--white);font-size:14px;text-transform:uppercase}
.topbar .dot{width:36px;height:36px;border-radius:50%;background:var(--gold);display:flex;align-items:center;justify-content:center}
.nav{position:absolute;left:116px;top:81px;width:984px;height:58px;background:var(--white);border-radius:30px;box-shadow:0 4px 14px rgba(0,0,0,.12)}
.nav a{position:absolute;top:21px;font-size:13px;font-weight:600;color:var(--ink);text-decoration:none;text-transform:uppercase}
.nav a.active::after{content:"";position:absolute;left:0;right:0;bottom:-20px;height:3px;background:var(--gold)}
.logo-badge{position:absolute;left:378px;top:-88px;width:208px;height:208px;border-radius:50%;background:var(--white);box-shadow:0 6px 16px rgba(0,0,0,.15);display:flex;flex-direction:column;align-items:center;justify-content:center;padding-top:70px}
.hero-eyebrow{position:absolute;left:118px;top:270px;color:var(--white);font-size:19px;text-transform:uppercase;display:flex;align-items:center;gap:12px}
.hero-eyebrow::after{content:"";width:40px;height:1px;background:var(--white)}
.hero h1{position:absolute;left:116px;top:302px;width:560px;color:var(--white);font-size:50px;line-height:54px;font-weight:700;text-transform:uppercase}

/* features */
.feature{position:absolute;text-align:center;color:var(--white);padding-top:58px}
.feature h3{font-size:18px;font-weight:700;text-transform:uppercase;margin-bottom:10px}
.feature p{font-size:12.5px;line-height:19px;padding:0 40px}
.feature .btn{left:50%;transform:translateX(-50%);font-size:11px;height:36px;width:136px}
.feature-icon{position:absolute;left:50%;top:-38px;transform:translateX(-50%);width:76px;height:76px;border-radius:50%;background:var(--gold);border:5px solid var(--white);display:flex;align-items:center;justify-content:center}

/* about */
.about h2{position:absolute;left:640px;top:1046px;font-size:40px;line-height:44px;font-weight:700;color:var(--slate-dark);text-transform:uppercase}
.about p{position:absolute;left:646px;top:1176px;width:480px;font-size:17px;line-height:29px;color:var(--ink)}

/* services */
.services-band{position:absolute;left:0;top:1578px;width:1200px;height:579px;background:var(--mist)}
.bump{position:absolute;border-radius:50%}
.service-card{position:absolute;top:1736px;width:246px;height:332px;border-radius:8px;overflow:hidden;border:1.5px solid #c9c9cc;background:var(--white);text-align:center}
.service-card.dark{background:var(--slate);border-color:var(--slate)}
.service-card .img{height:164px;border-radius:0 0 50% 50%/0 0 26px 26px}
.service-card .icon{position:absolute;left:50%;top:136px;transform:translateX(-50%);width:58px;height:58px;border-radius:50%;background:var(--gold);border:4px solid var(--white);display:flex;align-items:center;justify-content:center}
.service-card h4{margin-top:48px;font-size:15px;font-weight:600;color:var(--ink);padding:0 24px;line-height:19px}
.service-card.dark h4,.service-card.dark p{color:var(--white)}
.service-card p{font-size:11.5px;line-height:16px;color:var(--muted);padding:6px 28px 0}
.service-card .btn{left:50%;transform:translateX(-50%);bottom:16px;width:110px;height:30px;font-size:10px}
.service-card.dark .btn{background:transparent;border:1.5px solid var(--white)}

/* plans */
.plans-band{position:absolute;left:0;top:2157px;width:1200px;height:511px;background:var(--gold)}
.plans-band h2{position:absolute;left:0;top:108px;width:1200px;text-align:center;color:var(--white);font-size:34px;font-weight:700;text-transform:uppercase}
.plans-band p{position:absolute;left:200px;top:165px;width:800px;text-align:center;color:var(--white);font-size:16.5px;line-height:28px}
.plan-card{position:absolute;top:2421px;width:431px;height:457px;background:var(--white);border:1.5px solid #dcdcdf;border-radius:6px;overflow:hidden}
.plan-card .img{height:247px}
.plan-card h4{position:absolute;left:44px;top:286px;font-size:20px;font-weight:600;color:var(--ink)}
.plan-card .bar{position:absolute;left:0;top:282px;width:4px;height:34px;background:var(--gold)}
.plan-card p{position:absolute;left:44px;top:320px;width:370px;font-size:12.5px;line-height:20px;color:var(--muted)}
.plan-card .btn{left:36px;top:378px;width:138px;height:38px;font-size:11px}

/* why choose */
.reason{position:absolute;width:240px}
.reason h5{font-size:17px;font-weight:600;color:var(--ink);margin-bottom:4px}
.reason p{font-size:12px;line-height:17px;color:var(--muted)}
.reason-icon{position:absolute;width:50px;height:50px;border-radius:50%;background:var(--slate);display:flex;align-items:center;justify-content:center;transform:translate(-50%,-50%)}

/* testimonials */
.reviews-band{position:absolute;left:0;top:3497px;width:1200px;height:554px;background:var(--mist)}
.review{position:absolute;background:var(--white);text-align:center;box-shadow:0 4px 18px rgba(0,0,0,.06);overflow:hidden}
.stars{color:var(--gold);letter-spacing:3px}
.review p{color:var(--ink)}
.quote-mark{position:absolute;color:#c9c9cc;font-weight:700;font-family:Georgia,serif}
.arrow-btn{position:absolute;width:40px;height:40px;border-radius:50%;background:var(--gold);display:flex;align-items:center;justify-content:center}

/* booking */
.booking{position:absolute;left:110px;top:4095px;width:980px;height:550px;background:var(--slate-dark);border-radius:14px}
.booking h2{position:absolute;left:0;top:80px;width:980px;text-align:center;color:var(--white);font-size:34px;font-weight:700;text-transform:uppercase}
.field{position:absolute;background:var(--white);border-radius:3px;display:flex;align-items:center;gap:10px;padding:0 22px;font-size:14px;color:var(--muted)}

/* footer */
.footer-nav{position:absolute;top:4728px;display:flex;align-items:center;gap:22px;font-size:14px;font-weight:500;color:var(--ink);text-transform:uppercase}
.footer-nav .sep{width:5px;height:5px;border-radius:50%;background:var(--ink)}
.rule{position:absolute;left:135px;width:930px;height:1px;background:#d5d5d8}
.contact{position:absolute;top:4812px;display:flex;align-items:center;gap:14px}
.contact .dot{width:42px;height:42px;border-radius:50%;background:var(--gold);display:flex;align-items:center;justify-content:center}
.contact small{display:block;font-size:12.5px;color:var(--muted)}
.contact span{font-size:14px;color:var(--ink)}
.social{position:absolute;top:4814px;width:36px;height:36px;border-radius:50%}
</style>
</head>
<body>

<!-- HERO -->
<header class="hero">
  <div class="hero-photo" role="img" aria-label="Photo of a technician in white shirt and safety glasses fitting a ceiling light bulb"></div>
  <div class="hero-eyebrow">Wexbridge Home Services</div>
  <h1>Where Home Maintenance is Effortless</h1>
  <div class="btn btn-gold" style="left:116px;top:478px;width:284px;height:50px;font-size:15px">Book an Appointment</div>
</header>

<div class="topbar" style="left:140px">
  <span class="dot"><svg width="18" height="18" viewBox="0 0 24 24" fill="none" stroke="#fff" stroke-width="2"><rect x="3" y="5" width="18" height="16" rx="2"/><path d="M3 10h18M8 3v4M16 3v4"/></svg></span>
  Schedule Appointment
</div>
<div class="topbar" style="left:780px">
  <span class="dot"><svg width="18" height="18" viewBox="0 0 24 24" fill="#fff"><path d="M6.6 10.8a15 15 0 0 0 6.6 6.6l2.2-2.2c.3-.3.7-.4 1-.2 1.1.4 2.3.6 3.6.6.6 0 1 .4 1 1V20c0 .6-.4 1-1 1A17 17 0 0 1 3 4c0-.6.4-1 1-1h3.5c.6 0 1 .4 1 1 0 1.3.2 2.5.6 3.6.1.3 0 .7-.2 1z"/></svg></span>
  Call us now (+123) 555 0148
</div>

<nav class="nav">
  <a class="active" style="left:44px">Home</a>
  <a style="left:136px">About Us</a>
  <a style="left:258px">Services</a>
  <a style="left:634px">Contact</a>
  <div class="btn btn-gold" style="left:740px;top:9px;width:226px;height:40px;font-size:12px">Schedule Appointment</div>
  <div class="logo-badge">
    <div class="wordmark" style="font-size:27px">Wexbridge</div>
    <div class="wordmark" style="font-size:11px;margin-top:4px">Home Services</div>
  </div>
</nav>

<!-- FEATURES -->
<div class="feature" style="left:110px;top:698px;width:295px;height:201px;background:var(--slate)">
  <div class="feature-icon"><svg width="34" height="34" viewBox="0 0 24 24" fill="none" stroke="#fff" stroke-width="1.6"><circle cx="12" cy="9" r="5"/><path d="M9 13.5 7.5 21l4.5-2.5L16.5 21 15 13.5"/></svg></div>
  <h3>Why Us?</h3>
  <p>Lorem ipsum dolor sit amet, consectetur adipiscing elit sed</p>
  <div class="btn btn-ghost" style="top:134px">Read More ›</div>
</div>
<div class="feature" style="left:405px;top:683px;width:367px;height:231px;background:var(--gold);box-shadow:0 6px 18px rgba(0,0,0,.18)">
  <div class="feature-icon"><svg width="34" height="34" viewBox="0 0 24 24" fill="none" stroke="#fff" stroke-width="1.6"><rect x="6" y="2" width="12" height="20" rx="2"/><path d="M9 9h6M9 13h6M9 17h3"/></svg></div>
  <h3>Book a Service Now</h3>
  <p>Lorem ipsum dolor sit amet, consectetur adipiscing elit, sed do eiusmod temp</p>
  <div class="btn" style="top:156px;background:var(--slate-dark);color:#fff">Book Now ›</div>
</div>
<div class="feature" style="left:772px;top:698px;width:303px;height:201px;background:var(--slate)">
  <div class="feature-icon"><svg width="34" height="34" viewBox="0 0 24 24" fill="none" stroke="#fff" stroke-width="1.6"><path d="M3 11 12 4l9 7"/><path d="M5 10v10h14V10"/><path d="M10 20v-5h4v5"/></svg></div>
  <h3>Services</h3>
  <p>Lorem ipsum dolor sit amet, consectetur adipiscing elit ed do</p>
  <div class="btn btn-ghost" style="top:134px">Read More ›</div>
</div>

<!-- ABOUT -->
<section class="about">
  <div class="photo" role="img" aria-label="Photo of a technician in blue cap cleaning a wall-mounted air conditioner" style="left:96px;top:1017px;width:431px;height:395px;background:linear-gradient(135deg,#e9ecef,#b9c4cf 55%,#6d85a8)"></div>
  <div class="photo" role="img" aria-label="Photo of a smiling homeowner in a bright living room" style="left:340px;top:1250px;width:254px;height:233px;background:linear-gradient(135deg,#f3efe8,#d8cbb8 60%,#a58c6f);border:5px solid #fff"></div>
  <h2>About Wexbridge<br>Home Services</h2>
  <p>Lorem ipsum dolor sit amet, consectetur adipiscing elit, sed do eiusmod tempor incididunt ut labore et dolore magna aliqua. Quis ipsum suspendisse ultrices gravida. Risus commodo viverra maecenas accumsan lacus vel facilisis.</p>
  <div class="btn btn-gold" style="left:646px;top:1350px;width:189px;height:48px;font-size:14px">Learn More ›</div>
</section>

<!-- SERVICES -->
<div class="services-band"></div>
<div class="bump" style="left:532px;top:1540px;width:136px;height:136px;background:var(--mist)"></div>
<h2 class="section-title" style="top:1638px">Our Services</h2>
<div class="swoosh" style="left:520px;top:1694px;width:160px"></div>

<div class="service-card" style="left:87px">
  <div class="img" role="img" aria-label="Photo of a dryer vent grille" style="background:linear-gradient(160deg,#d6d6d6,#555 60%,#2b2b2b)"></div>
  <div class="icon"><svg width="26" height="26" viewBox="0 0 24 24" fill="none" stroke="#fff" stroke-width="1.8"><rect x="4" y="4" width="16" height="16" rx="2"/><path d="M8 9h8M8 12h8M8 15h8"/></svg></div>
  <h4>Dryer Vent Cleaning</h4>
  <p>Lorem ipsum dolor sit amet, consectetur adipiscing elit</p>
  <div class="btn btn-slate">Learn More</div>
</div>
<div class="service-card dark" style="left:353px">
  <div class="img" role="img" aria-label="Photo of gloved hands cleaning an air conditioner unit" style="background:linear-gradient(160deg,#eef2f6,#8fb4e0 55%,#3d6fb8)"></div>
  <div class="icon"><svg width="26" height="26" viewBox="0 0 24 24" fill="none" stroke="#fff" stroke-width="1.8"><rect x="3" y="5" width="18" height="9" rx="2"/><path d="M7 18v2M12 18v3M17 18v2"/></svg></div>
  <h4>AC Cleaning</h4>
  <p>Lorem ipsum dolor sit amet, consectetur adipiscing elit</p>
  <div class="btn">Learn More</div>
</div>
<div class="service-card" style="left:617px">
  <div class="img" role="img" aria-label="Photo of a worker replacing a ceiling light bulb" style="background:linear-gradient(160deg,#f0ece6,#b8b3ad 55%,#4d5563)"></div>
  <div class="icon"><svg width="26" height="26" viewBox="0 0 24 24" fill="none" stroke="#fff" stroke-width="1.8"><path d="M9 18h6M10 21h4"/><path d="M12 3a6 6 0 0 0-3.5 10.9c.5.4.5 1 .5 1.6V16h6v-.5c0-.6 0-1.2.5-1.6A6 6 0 0 0 12 3z"/></svg></div>
  <h4>Difficult-to-Reach Light Bulb replacement</h4>
  <p>Lorem ipsum dolor sit amet con</p>
  <div class="btn btn-slate">Learn More</div>
</div>
<div class="service-card" style="left:883px">
  <div class="img" role="img" aria-label="Photo of a wooden toolbox with woodworking tools" style="background:linear-gradient(160deg,#d9c3a4,#a87a4c 55%,#6a4526)"></div>
  <div class="icon"><svg width="26" height="26" viewBox="0 0 24 24" fill="none" stroke="#fff" stroke-width="1.8"><path d="M4 20 14 10M14 4l6 6-3 3-6-6z"/><path d="M5 5l14 14"/></svg></div>
  <h4>Wood Repair</h4>
  <p>Lorem ipsum dolor sit amet, consectetur adipiscing elit</p>
  <div class="btn btn-slate">Learn More</div>
</div>

<!-- PLANS -->
<div class="abs" style="left:610px;top:2132px;width:1.5px;height:68px;background:var(--slate)"></div>
<section class="plans-band">
  <h2>Home Maintenance Plans</h2>
  <p>Lorem ipsum dolor sit amet, consectetur adipiscing elit, sed do eiusmod tempor incididunt ut labore et dolore magna aliqua. Quis ipsum suspendisse</p>
</section>
<div class="plan-card" style="left:160px">
  <div class="img" role="img" aria-label="Photo of hands fitting a smoke detector to the ceiling" style="background:linear-gradient(160deg,#f4f4f4,#cfcfcf 50%,#c79a7b)"></div>
  <span class="bar"></span>
  <h4>Fire Safety Checks</h4>
  <p>Lorem ipsum dolor sit amet, consectetur adipiscing elit, sed do eiusmod tempor incididunt ut labore e</p>
  <div class="btn btn-slate">Book Now</div>
</div>
<div class="plan-card" style="left:615px">
  <div class="img" role="img" aria-label="Photo of an older woman replacing a ceiling air filter" style="background:linear-gradient(160deg,#c9a98c,#e8e8e8 45%,#f7f7f7)"></div>
  <span class="bar"></span>
  <h4>Filter Replacement</h4>
  <p>Lorem ipsum dolor sit amet, consectetur adipiscing elit, sed do eiusmod tempor incididunt ut labore e</p>
  <div class="btn btn-slate">Book Now</div>
</div>

<!-- WHY CHOOSE -->
<h2 class="section-title" style="top:2940px;font-size:33px">Why Choose Wexbridge</h2>
<div class="swoosh" style="left:530px;top:2996px;width:140px"></div>
<svg class="abs" style="left:0;top:3100px" width="1200" height="400" viewBox="0 0 1200 400">
  <path d="M282 397 A318 318 0 0 1 918 397" fill="none" stroke="#cfcfd2" stroke-width="1.5"/>
  <path d="M318 397 A282 282 0 0 1 882 397 Z" fill="#e3ab2c"/>
</svg>
<div class="reason" style="left:478px;top:3060px;text-align:center"><h5>Expertise You Can Trust</h5><p>Lorem ipsum dolor sit amet,<br>consectetur adipiscing</p></div>
<div class="reason" style="left:136px;top:3176px;text-align:right;width:240px"><h5>Hassle-Free Scheduling</h5><p>Lorem ipsum dolor sit amet,<br>consectetur adipiscing</p></div>
<div class="reason" style="left:28px;top:3314px;text-align:right;width:240px"><h5>Trust-focused</h5><p>Lorem ipsum dolor sit amet,<br>consectetur adipiscing</p></div>
<div class="reason" style="left:834px;top:3192px"><h5>Reliable &amp; On-Time</h5><p>Lorem ipsum dolor sit amet,<br>consectetur adipiscing</p></div>
<div class="reason" style="left:934px;top:3314px;width:260px"><h5>Comprehensive Home Care</h5><p>Lorem ipsum dolor sit amet,<br>consectetur adipiscing</p></div>

<div class="reason-icon" style="left:598px;top:3164px"><svg width="24" height="24" viewBox="0 0 24 24" fill="none" stroke="#fff" stroke-width="1.7"><path d="M3 12l4-4 5 2 5-2 4 4-6 6-3-3-3 3z"/></svg></div>
<div class="reason-icon" style="left:424px;top:3212px"><svg width="24" height="24" viewBox="0 0 24 24" fill="none" stroke="#fff" stroke-width="1.7"><rect x="3" y="5" width="18" height="16" rx="2"/><path d="M3 10h18M8 3v4M16 3v4"/></svg></div>
<div class="reason-icon" style="left:312px;top:3341px"><svg width="24" height="24" viewBox="0 0 24 24" fill="none" stroke="#fff" stroke-width="1.7"><path d="M12 3l8 3v6c0 5-4 8-8 9-4-1-8-4-8-9V6z"/><path d="M8.5 12l2.5 2.5 4.5-4.5"/></svg></div>
<div class="reason-icon" style="left:785px;top:3222px"><svg width="24" height="24" viewBox="0 0 24 24" fill="none" stroke="#fff" stroke-width="1.7"><circle cx="12" cy="12" r="9"/><path d="M12 7v5l3 2"/></svg></div>
<div class="reason-icon" style="left:889px;top:3341px"><svg width="24" height="24" viewBox="0 0 24 24" fill="none" stroke="#fff" stroke-width="1.7"><path d="M3 11 12 4l9 7"/><path d="M5 10v10h14V10"/></svg></div>

<!-- TESTIMONIALS -->
<section class="reviews-band">
  <h2 class="section-title" style="top:62px;font-size:35px">What People Says</h2>
</section>
<div class="review" style="left:154px;top:3684px;width:220px;height:209px;padding:24px 10px 0 40px;text-align:right">
  <div class="stars" style="font-size:16px">★★</div>
  <p style="font-size:12px;line-height:19px;margin-top:6px">"Lorem ipsum dolor sit a elit, sed do eiusmod ter dolore magna aliqua. ( tices gravida. Risus com cumsan lac</p>
</div>
<div class="review" style="left:826px;top:3684px;width:164px;height:209px;padding:24px 20px 0 0;text-align:left">
  <div class="stars" style="font-size:16px;padding-left:16px">★★</div>
  <p style="font-size:12px;line-height:19px;margin-top:6px;padding-left:16px">, consectetur adipiscing incididunt ut labore et ipsum suspendisse ul- do viverra maecenas ac- el facilisis"</p>
  <span class="quote-mark" style="right:14px;bottom:-20px;font-size:80px">”</span>
</div>
<div class="review" style="left:357px;top:3655px;width:486px;height:265px;padding:34px 42px 0;box-shadow:0 6px 24px rgba(0,0,0,.1)">
  <div class="stars" style="font-size:22px">★★★★★</div>
  <p style="font-size:15px;line-height:24px;margin-top:8px">"Lorem ipsum dolor sit amet, consectetur adipiscing elit, sed do eiusmod tempor incididunt ut labore et dolore magna aliqua. Quis ipsum suspendisse ultrices gravida. Risus commodo viverra maecenas accumsan lacus vel facilisis"</p>
  <p style="font-size:14px;font-weight:600;margin-top:16px">Mara Ellison</p>
  <span class="quote-mark" style="right:36px;bottom:-36px;font-size:110px">”</span>
</div>
<div class="arrow-btn" style="left:551px;top:3952px"><svg width="18" height="18" viewBox="0 0 24 24" fill="none" stroke="#fff" stroke-width="2.4"><path d="M19 12H5M11 6l-6 6 6 6"/></svg></div>
<div class="arrow-btn" style="left:605px;top:3952px"><svg width="18" height="18" viewBox="0 0 24 24" fill="none" stroke="#fff" stroke-width="2.4"><path d="M5 12h14M13 6l6 6-6 6"/></svg></div>

<!-- BOOKING -->
<section class="booking">
  <h2>Book an Appointment</h2>
  <div class="swoosh" style="left:410px;top:132px;width:160px;background:#fff;height:4px"></div>
  <div class="field" style="left:133px;top:170px;width:363px;height:52px"><svg width="14" height="14" viewBox="0 0 24 24" fill="#9a9a9e"><circle cx="12" cy="8" r="5"/><path d="M3 22c0-5 4-8 9-8s9 3 9 8z"/></svg>First name</div>
  <div class="field" style="left:509px;top:170px;width:365px;height:52px"><svg width="14" height="14" viewBox="0 0 24 24" fill="#9a9a9e"><circle cx="12" cy="8" r="5"/><path d="M3 22c0-5 4-8 9-8s9 3 9 8z"/></svg>Last name</div>
  <div class="field" style="left:133px;top:235px;width:363px;height:53px"><svg width="14" height="14" viewBox="0 0 24 24" fill="#9a9a9e"><path d="M6.6 10.8a15 15 0 0 0 6.6 6.6l2.2-2.2c.3-.3.7-.4 1-.2 1.1.4 2.3.6 3.6.6.6 0 1 .4 1 1V20c0 .6-.4 1-1 1A17 17 0 0 1 3 4c0-.6.4-1 1-1h3.5c.6 0 1 .4 1 1 0 1.3.2 2.5.6 3.6.1.3 0 .7-.2 1z"/></svg>Email address</div>
  <div class="field" style="left:509px;top:235px;width:365px;height:53px"><svg width="14" height="14" viewBox="0 0 24 24" fill="#9a9a9e"><rect x="3" y="5" width="18" height="14" rx="2"/></svg>Phone</div>
  <div class="field" style="left:133px;top:299px;width:741px;height:97px;align-items:flex-start;padding-top:16px"><svg width="14" height="14" viewBox="0 0 24 24" fill="#9a9a9e"><path d="M3 5h18v11H8l-5 4z"/></svg>Leave Message</div>
  <div class="btn btn-gold" style="left:407px;top:421px;width:177px;height:48px;font-size:14px">Book Now ›</div>
</section>

<!-- FOOTER -->
<div class="bump" style="left:510px;top:4608px;width:180px;height:180px;background:var(--white)"></div>
<div class="abs" style="left:480px;top:4718px;width:240px">
  <div class="wordmark" style="font-size:29px">Wexbridge</div>
  <div class="wordmark" style="font-size:13px;margin-top:4px">Home Services</div>
</div>
<div class="footer-nav" style="left:142px">Home<span class="sep"></span>About Us<span class="sep"></span>Services</div>
<div class="footer-nav" style="left:777px">Why Us<span class="sep"></span>Contact<span class="sep"></span>Book Now</div>
<div class="rule" style="top:4790px"></div>
<div class="contact" style="left:156px">
  <span class="dot"><svg width="20" height="20" viewBox="0 0 24 24" fill="#fff"><path d="M6.6 10.8a15 15 0 0 0 6.6 6.6l2.2-2.2c.3-.3.7-.4 1-.2 1.1.4 2.3.6 3.6.6.6 0 1 .4 1 1V20c0 .6-.4 1-1 1A17 17 0 0 1 3 4c0-.6.4-1 1-1h3.5c.6 0 1 .4 1 1 0 1.3.2 2.5.6 3.6.1.3 0 .7-.2 1z"/></svg></span>
  <div><small>Phone Number</small><span>(+123) 555 0148</span></div>
</div>
<div class="contact" style="left:527px">
  <span class="dot"><svg width="20" height="20" viewBox="0 0 24 24" fill="none" stroke="#fff" stroke-width="2"><rect x="3" y="5" width="18" height="14" rx="2"/><path d="M3 7l9 6 9-6"/></svg></span>
  <div><small>Email adress</small><span>info@wexbridgehomeservices.com</span></div>
</div>
<span class="social" style="left:930px;background:var(--gold)" aria-label="Social link"></span>
<span class="social" style="left:974px;background:var(--slate)" aria-label="Social link"></span>
<span class="social" style="left:1018px;background:var(--slate)" aria-label="Social link"></span>
<span class="social" style="left:1062px;background:var(--slate)" aria-label="Social link"></span>
<div class="rule" style="top:4877px"></div>
<div class="abs" style="left:0;top:4906px;width:1200px;text-align:center;font-size:13px;color:var(--muted)">Copyright © 2025 Wexbridge Home Services . All Right Reserved</div>
<div class="abs" style="left:1008px;top:4900px;width:108px;height:30px;border-radius:15px;background:#e4e4e6;display:flex;align-items:center;padding-left:14px;font-size:10px;font-weight:600;color:var(--ink)">GO TO TOP
  <span style="position:absolute;right:0;top:0;width:30px;height:30px;border-radius:50%;background:var(--slate);display:flex;align-items:center;justify-content:center"><svg width="12" height="12" viewBox="0 0 24 24" fill="none" stroke="#fff" stroke-width="2.6"><path d="M12 20V4M6 10l6-6 6 6"/></svg></span>
</div>

</body>
</html>
```